Leadership Conference Graphic Design Image

The Theme of our Conference is "Navigating Change. Driving Success." Attached is an AI example - What we are looking for is something along the lines of this image, but with realistic roads, a realistic semi truck (without being able to tell the make of the semi truck) and with the semi truck leaving dark skies and heading towards positive sunnier type skies. Please don't use the "Pinecrest Haulers Guild Yearly Convention" verbiage - Our event is called "Leadership Conference and Vendor Showcase". I've also attached our logo which we would like on the image as well - And we would like both vertical and horizontal designs. We will be using this on our stage and in printed materials.

```html
<!DOCTYPE html>
<html lang="en">
<head>
<meta charset="utf-8">
<title>Navigating Change. Driving Success. – Leadership Conference and Vendor Showcase</title>
<link rel="stylesheet" href="https://fonts.googleapis.com/css2?family=Barlow+Condensed:wght@600;700&family=Roboto+Condensed:wght@500&display=swap">
<style>
  :root {
    --page: #ffffff;
    --navy-deep: #14294a;
    --navy: #1f3d66;
    --sky-blue: #3f72a8;
    --haze: #8fa9c4;
    --sun-gold: #f7c548;
    --sun-core: #fff3c4;
    --white: #ffffff;
    --headline-gold: #f5bd22;
    --alert-gold: #f2b51c;
    --pin-red: #c8252b;
    --compass-blue: #1f4f94;
  }
  * { margin: 0; padding: 0; box-sizing: border-box; }
  html, body {
    width: 1200px;
    height: 1200px;
    overflow: hidden;
    background: var(--page);
  }
  .poster {
    position: absolute;
    left: 158px;
    top: 149px;
    width: 884px;
    height: 884px;
    overflow: hidden;
  }
  .scene-photo {
    position: absolute;
    inset: 0;
    background:
      radial-gradient(circle at 92% 62%, var(--sun-core) 0%, var(--sun-gold) 12%, rgba(247,197,72,0.55) 26%, rgba(247,197,72,0) 48%),
      radial-gradient(ellipse at 70% 90%, rgba(190,170,90,0.55) 0%, rgba(190,170,90,0) 45%),
      linear-gradient(105deg, var(--navy-deep) 0%, var(--navy) 30%, var(--sky-blue) 58%, var(--haze) 78%, #d9b46a 100%);
  }
  .route-lines {
    position: absolute;
    inset: 0;
  }
  .route-lines path {
    fill: none;
    stroke: var(--white);
    stroke-width: 2.2;
    stroke-dasharray: 6 5;
    opacity: 0.85;
  }
  .icon { position: absolute; }
  .icon-compass { left: 255px; top: 56px; width: 94px; height: 94px; }
  .icon-alert { left: 458px; top: 38px; width: 56px; height: 48px; }
  .icon-pin { left: 662px; top: 56px; width: 62px; height: 88px; }

  .headline {
    position: absolute;
    left: 0;
    width: 884px;
    text-align: center;
    font-family: "Barlow Condensed", "Arial Narrow", sans-serif;
    font-weight: 700;
    font-size: 70px;
    line-height: 1;
    text-shadow: 0 3px 10px rgba(10, 25, 50, 0.55);
  }
  .headline-change { top: 355px; color: var(--white); padding-left: 0; left: -0px; }
  .headline-success { top: 421px; color: var(--headline-gold); }
  .headline-rule {
    position: absolute;
    left: 190px;
    top: 498px;
    width: 504px;
    height: 2px;
    background: linear-gradient(90deg, rgba(255,255,255,0), rgba(255,255,255,0.85) 20%, rgba(255,255,255,0.85) 80%, rgba(255,255,255,0));
  }
  .event-title {
    position: absolute;
    left: 0;
    top: 504px;
    width: 884px;
    text-align: center;
    font-family: "Roboto Condensed", "Arial Narrow", sans-serif;
    font-weight: 500;
    font-size: 33px;
    line-height: 40px;
    letter-spacing: 1px;
    color: var(--white);
    text-shadow: 0 2px 6px rgba(10, 25, 50, 0.5);
  }
  .org-name {
    position: absolute;
    left: 38px;
    top: 790px;
    width: 300px;
    font-family: "Barlow Condensed", "Arial Narrow", sans-serif;
    font-weight: 700;
    font-size: 34px;
    line-height: 36px;
    color: var(--white);
    text-transform: uppercase;
  }
</style>
</head>
<body>
<main class="poster">
  <div class="scene-photo" role="img" aria-label="Driver's hands on a truck steering wheel at left under dark storm clouds, opening to a sunlit highway where a white semi truck heads toward a bright sunrise over mountains"></div>

  <svg class="route-lines" viewBox="0 0 884 884" aria-hidden="true">
    <path d="M40 330 Q 300 -20 700 40 Q 860 80 884 170"/>
    <path d="M30 420 Q 260 60 520 80 Q 760 100 884 380"/>
    <path d="M0 500 Q 150 300 360 220 Q 600 150 884 420"/>
    <path d="M0 360 Q 230 560 560 700 Q 740 790 884 840"/>
    <path d="M0 690 Q 300 700 520 760 Q 640 800 700 884"/>
    <path d="M420 884 Q 640 790 884 730"/>
    <path d="M884 560 Q 800 520 600 470"/>
  </svg>

  <svg class="icon icon-compass" viewBox="0 0 94 94" aria-hidden="true">
    <circle cx="47" cy="47" r="45" fill="var(--compass-blue)" stroke="var(--white)" stroke-width="2"/>
    <circle cx="47" cy="47" r="33" fill="none" stroke="rgba(255,255,255,0.45)" stroke-width="1.5"/>
    <line x1="47" y1="16" x2="47" y2="78" stroke="rgba(255,255,255,0.45)" stroke-width="1.5"/>
    <line x1="16" y1="47" x2="78" y2="47" stroke="rgba(255,255,255,0.45)" stroke-width="1.5"/>
    <polygon points="66,26 52,52 42,42" fill="var(--alert-gold)"/>
    <polygon points="28,68 42,42 52,52" fill="var(--white)"/>
  </svg>

  <svg class="icon icon-alert" viewBox="0 0 56 48" aria-hidden="true">
    <path d="M28 3 L53 45 H3 Z" fill="var(--alert-gold)" stroke="var(--alert-gold)" stroke-width="4" stroke-linejoin="round"/>
    <rect x="25.5" y="17" width="5" height="16" rx="2" fill="#3a2c05"/>
    <circle cx="28" cy="38.5" r="3" fill="#3a2c05"/>
  </svg>

  <svg class="icon icon-pin" viewBox="0 0 62 88" aria-hidden="true">
    <path d="M31 2 C14 2 2 15 2 31 C2 52 31 86 31 86 C31 86 60 52 60 31 C60 15 48 2 31 2 Z" fill="var(--pin-red)"/>
    <circle cx="31" cy="30" r="12" fill="var(--white)"/>
  </svg>

  <h1>
    <span class="headline headline-change">NAVIGATING CHANGE.</span>
    <span class="headline headline-success">DRIVING SUCCESS.</span>
  </h1>
  <div class="headline-rule"></div>
  <p class="event-title">Leadership Conference and<br>Vendor Showcase</p>

  <p class="org-name">Pinecrest Haulers<br>Guild</p>
</main>
</body>
</html>
```